Saffron Lotus Court Business Card

I am looking for a business card desgined for my restaurant. It is an Indian restaurant, we are looking for something thats modern, yet traditional with the indian culture, we are looking for colors that match our logo. The logo is a design of the building with the name of the restaurant. for more information on the restaurant go to www.saffronlotuscourt.example

Industry/Entity Type

Indian Restaurant

Contact Information for Business Card

we are looking for somthing thats modern, yet traditional with the indian culture, we are looking for colors that match our logo. The logo is a design of the building with the name of the restaurant. for more information on the restaurant go to www.saffronlotuscourt.example

Requirements
Must have
• The logo that is attached,
• Name: Harjot Banwal,
• address of the restaurant: 2917 West Tamarind Ave, Phoenix, Arizona, 85047
• Phone: (602) 517-3094
• Fax: (602) 768-2145
• Restaurant Catering Banquet
• Website: www.SaffronLotusCourt.example
Nice to have
• wanted to get something that goes with the theme of the restaurant, which is traditional but also keep a very professional and modern touch

```html
<!DOCTYPE html>
<html lang="en">
<head>
<meta charset="utf-8">
<title>Saffron Lotus Court – Business Card</title>
<link rel="stylesheet" href="https://fonts.googleapis.com/css2?family=Lato:wght@400;700&display=swap">
<style>
  :root {
    --page-bg: #e4e5e7;
    --band-black: #1c1b17;
    --face-white: #fbfbfa;
    --pattern-grey: #ecebea;
    --gold: #c9a862;
    --gold-light: #efe2b8;
    --cream: #f1e6c4;
    --brand-red: #c43d1d;
    --ink: #232323;
    --back-dark: #262622;
    --back-pattern: #2f2f2a;
    --logo-gold: #cbb37c;
  }
  * { box-sizing: border-box; margin: 0; padding: 0; }
  html, body { width: 1200px; height: 800px; overflow: hidden; }
  body {
    background: var(--page-bg);
    font-family: "Lato", Arial, sans-serif;
    color: var(--ink);
    position: relative;
  }
  .card {
    position: absolute;
    top: 50px;
    width: 400px;
    height: 700px;
    box-shadow: 0 10px 28px rgba(0,0,0,0.25);
    overflow: hidden;
  }
  .card--front { left: 170px; }
  .card--back { left: 630px; }
  .card__art { position: absolute; inset: 0; width: 400px; height: 700px; }

  .brand {
    position: absolute;
    left: 0; right: 0;
    text-align: center;
    font-weight: 700;
    text-transform: uppercase;
    letter-spacing: 2px;
  }
  .brand--front {
    top: 86px;
    color: var(--brand-red);
    font-size: 34px;
    line-height: 38px;
  }
  .brand--back {
    top: 270px;
    color: var(--logo-gold);
    font-size: 38px;
    line-height: 44px;
  }

  .contact {
    position: absolute;
    top: 258px;
    left: 0; right: 0;
    text-align: center;
  }
  .contact__name {
    font-size: 31px;
    font-weight: 400;
    letter-spacing: 1.5px;
    text-transform: uppercase;
    margin-bottom: 22px;
  }
  .contact__line {
    font-size: 19px;
    line-height: 26px;
    display: flex;
    flex-direction: column;
    align-items: center;
  }
  .contact__icon { width: 14px; height: 14px; margin-bottom: 2px; }
  .contact__label { font-size: 12px; line-height: 14px; }
  .contact__group { margin-bottom: 8px; }
  .divider {
    width: 300px;
    margin: 12px auto 12px;
    border-top: 2px dotted var(--ink);
  }
  .services {
    font-size: 16px;
    font-weight: 700;
    letter-spacing: 0.5px;
    text-transform: uppercase;
  }
  .address { font-size: 21px; line-height: 27px; }
</style>
</head>
<body>

<section class="card card--front" aria-label="Business card front">
  <svg class="card__art" viewBox="0 0 400 700">
    <rect width="400" height="700" fill="var(--band-black)"/>
    <path d="M0 100 Q200 10 400 100 L400 600 Q200 690 0 600 Z" fill="var(--gold)"/>
    <path d="M0 112 Q200 24 400 112 L400 588 Q200 676 0 588 Z" fill="var(--gold-light)"/>
    <path d="M0 118 Q200 32 400 118 L400 582 Q200 668 0 582 Z" fill="var(--face-white)"
          role="img" aria-label="Faint grey damask pattern on white card face"/>
  </svg>

  <div class="brand brand--front">Saffron<br>Lotus<br>Court</div>

  <div class="contact">
    <p class="contact__name">Harjot Banwal</p>

    <div class="contact__line contact__group">
      <svg class="contact__icon" viewBox="0 0 14 14" aria-hidden="true">
        <rect x="1" y="4" width="12" height="9" rx="1.5" fill="var(--ink)"/>
        <rect x="3" y="1" width="8" height="4" rx="1" fill="var(--ink)"/>
      </svg>
      <span>(602) 517-3094</span>
    </div>
    <div class="contact__line contact__group">
      <span class="contact__label">Fax</span>
      <span>(602) 768-2145</span>
    </div>
    <div class="contact__line">
      <svg class="contact__icon" viewBox="0 0 14 14" aria-hidden="true">
        <circle cx="7" cy="7" r="6" fill="none" stroke="var(--ink)" stroke-width="1.4"/>
        <ellipse cx="7" cy="7" rx="2.6" ry="6" fill="none" stroke="var(--ink)" stroke-width="1.2"/>
        <line x1="1" y1="7" x2="13" y2="7" stroke="var(--ink)" stroke-width="1.2"/>
      </svg>
      <span>www.SaffronLotusCourt.example</span>
    </div>

    <div class="divider"></div>

    <p class="services">Restaurant Catering Banquet</p>
    <p class="address">2917 West Tamarind Ave,<br>Phoenix, Arizona, 85047</p>
  </div>
</section>

<section class="card card--back" aria-label="Business card back">
  <svg class="card__art" viewBox="0 0 400 700">
    <rect width="400" height="700" fill="var(--band-black)"/>
    <path d="M0 100 Q200 10 400 100 L400 600 Q200 690 0 600 Z" fill="var(--cream)"/>
    <path d="M0 112 Q200 24 400 112 L400 588 Q200 676 0 588 Z" fill="var(--back-dark)"
          role="img" aria-label="Dark tone-on-tone damask pattern"/>
  </svg>

  <div class="brand brand--back">Saffron<br>Lotus<br>Court</div>
</section>

</body>
</html>
```